Ductless Mini Split Business Website

Amber Kite Services is looking to design an eye catching educational website about installing Ductless mini splits.

Similar to this company.
https://www.cedarcoolair.com/

```html
<!DOCTYPE html>
<html lang="en">
<head>
<meta charset="utf-8">
<title>Amber Kite Services — Ductless Experts</title>
<link href="https://fonts.googleapis.com/css2?family=Poppins:wght@400;500;600;800;900&family=Oswald:wght@400&family=Lato:ital,wght@0,400;1,400&display=swap" rel="stylesheet">
<style>
:root{
  --yellow:#f7c600;
  --yellow-dark:#e8b400;
  --ink:#111111;
  --text:#222222;
  --muted:#8a8a8a;
  --light:#f4f4f4;
  --photo:#c9cdd2;
  --photo-dark:#8e949b;
  --white:#ffffff;
}
*{margin:0;padding:0;box-sizing:border-box}
html,body{width:1200px;height:4031px;overflow:hidden;background:var(--white)}
body{position:relative;font-family:'Poppins',sans-serif;color:var(--text)}
.abs{position:absolute}
.photo{background:linear-gradient(135deg,var(--photo),var(--photo-dark))}
.btn{position:absolute;display:flex;align-items:center;justify-content:center;border-radius:30px;font-family:'Poppins',sans-serif;font-weight:500;text-transform:uppercase;font-size:16px;color:var(--ink);background:linear-gradient(180deg,var(--yellow),var(--yellow-dark));box-shadow:0 4px 0 rgba(0,0,0,.12)}
.btn--dark{background:var(--ink);color:var(--white)}
.eyebrow{position:absolute;font-size:17px;font-weight:500;text-transform:uppercase;color:var(--ink)}
.heading{position:absolute;font-family:'Oswald',sans-serif;font-size:44px;color:var(--ink);white-space:nowrap}
.center{left:0;width:1200px;text-align:center}
.lorem{font-family:'Lato',sans-serif;color:var(--muted)}

/* header */
.brand{left:78px;top:34px;display:flex;align-items:center;gap:10px;font-weight:800;font-size:21px;color:var(--ink)}
.brand__dot{width:30px;height:30px;border-radius:50%;background:var(--yellow)}
.phone{left:346px;top:39px;width:186px;height:50px;font-size:17px;text-transform:none;gap:10px}
.nav{top:56px;display:flex;font-size:14px;color:#555;text-transform:uppercase}
.nav a{position:absolute;white-space:nowrap;text-decoration:none;color:#555}
.nav a.is-active{color:var(--ink)}

/* hero */
.hero-art{left:500px;top:-200px}
.hero__title{left:78px;top:205px;font-weight:900;font-size:50px;line-height:53px;color:var(--ink);text-transform:uppercase}
.hero__text{left:78px;top:328px;width:400px;font-family:'Lato',sans-serif;font-style:italic;font-size:18px;line-height:29px;color:#555}

/* about */
.about__text{left:624px;top:836px;width:500px;font-size:14px;line-height:27px}

/* cards */
.card{position:absolute;top:1156px;width:333px;height:363px;background:var(--white);box-shadow:0 2px 10px rgba(0,0,0,.12);border-radius:4px;overflow:hidden}
.card__img{height:218px}
.card__title{position:absolute;left:33px;top:246px;font-size:20px;font-weight:500;color:var(--ink)}
.card .btn{left:31px;top:293px;height:39px;padding:0 20px;font-size:13px}

/* services */
.service{position:absolute;top:1728px;width:240px;text-align:center}
.service__icon{width:94px;height:94px;margin:0 auto;border-radius:50%;background:var(--white);box-shadow:0 2px 8px rgba(0,0,0,.12);display:flex;align-items:center;justify-content:center}
.service__icon.is-active{background:linear-gradient(180deg,var(--yellow),var(--yellow-dark))}
.service__title{margin-top:26px;font-size:19px;font-weight:500;color:var(--ink)}
.service__text{margin-top:14px;font-size:14px;line-height:23px}

/* why */
.feature{position:absolute;left:77px;width:480px;height:84px}
.feature__icon{position:absolute;left:0;top:0;width:84px;height:84px;border-radius:50%;display:flex;align-items:center;justify-content:center;background:linear-gradient(135deg,#3a3a3a,#000)}
.feature__icon.is-yellow{background:linear-gradient(180deg,var(--yellow),var(--yellow-dark))}
.feature__title{position:absolute;left:117px;top:-4px;font-size:19px;font-weight:500;color:var(--ink)}
.feature__text{position:absolute;left:117px;top:30px;width:340px;font-size:13px;line-height:23px}

/* testimonial */
.quote{left:211px;top:2800px;width:779px;height:324px;background:var(--white);box-shadow:0 2px 12px rgba(0,0,0,.1)}
.quote__text{position:absolute;left:50px;top:50px;width:679px;text-align:center;font-family:'Lato',sans-serif;font-style:italic;font-size:18px;line-height:31px;color:#777}
.quote__name{position:absolute;left:0;width:779px;top:200px;text-align:center;font-size:19px;color:var(--ink)}

/* newsletter */
.news{left:391px;top:3281px;width:732px;height:311px;background:linear-gradient(90deg,#2a2a2a 0%,#000 35%)}
.news__title{position:absolute;left:150px;top:50px;font-family:'Oswald',sans-serif;font-size:44px;color:var(--white)}
.news__text{position:absolute;left:150px;top:118px;width:490px;font-size:14px;line-height:27px;color:#ddd}
.news__field{position:absolute;left:149px;top:194px;width:540px;height:59px;background:var(--white);border-radius:30px;display:flex;align-items:center;padding-left:20px;gap:14px;font-family:'Lato',sans-serif;font-style:italic;font-size:14px;color:#555}
.news .btn{left:540px;top:197px;width:145px;height:53px}

/* footer */
.footer-brand{left:0;width:1200px;top:3690px;display:flex;justify-content:center;align-items:center;gap:10px;font-weight:800;font-size:21px;color:var(--ink)}
.footer-links{top:3778px;font-size:15px;color:#777;word-spacing:4px}
.social{position:absolute;top:3831px;width:44px;height:44px;border-radius:50%}
.copyright{left:0;width:1200px;top:3935px;height:96px;background:var(--light);display:flex;align-items:center;justify-content:center;font-size:12px;color:#888}
.copyright b{font-weight:600;color:#555}
</style>
</head>
<body>

<!-- hero artwork -->
<svg class="abs hero-art" width="700" height="855" viewBox="0 0 700 855" aria-hidden="true">
  <circle cx="452" cy="455" r="418" fill="var(--yellow)"/>
</svg>
<div class="abs photo" role="img" aria-label="Technician on a ladder replacing the filter of a ceiling air unit" style="left:543px;top:-154px;width:808px;height:808px;border-radius:50%"></div>

<header>
  <div class="abs brand"><span class="brand__dot"></span>Amber Kite Services</div>
  <div class="btn phone">
    <svg width="20" height="20" viewBox="0 0 24 24"><path fill="var(--ink)" d="M6.6 10.8a15 15 0 0 0 6.6 6.6l2.2-2.2a1 1 0 0 1 1-.25 11.4 11.4 0 0 0 3.6.57 1 1 0 0 1 1 1V20a1 1 0 0 1-1 1A17 17 0 0 1 3 4a1 1 0 0 1 1-1h3.5a1 1 0 0 1 1 1c0 1.25.2 2.45.57 3.57a1 1 0 0 1-.25 1z"/></svg>
    123.456.7890
  </div>
  <nav class="abs nav">
    <a class="is-active" style="left:624px">Home</a>
    <a style="left:696px">About Us</a>
    <a style="left:793px">Services</a>
    <a style="left:886px">Why Choose Us</a>
    <a style="left:1028px">Contact Us</a>
  </nav>
</header>

<section class="hero">
  <h1 class="abs hero__title">Ductless Does<br>It Better</h1>
  <p class="abs hero__text">Lorem ipsum dolor sit amet, consectetur adipiscing elit, sed do eiusmod tempor incididunt ut labore et dolore magna aliqua.</p>
  <a class="btn" style="left:77px;top:449px;width:166px;height:50px">Our Services</a>
  <a class="btn btn--dark" style="left:255px;top:449px;width:166px;height:50px">Contact Us</a>
</section>

<section class="about">
  <div class="abs" style="left:86px;top:627px;width:460px;height:465px;border-radius:50%;background:var(--yellow)"></div>
  <div class="abs photo" role="img" aria-label="Technician kneeling to install a wall heating unit with tools on the floor" style="left:76px;top:625px;width:448px;height:448px;border-radius:50%"></div>
  <p class="eyebrow" style="left:624px;top:718px">About Our Company</p>
  <h2 class="heading" style="left:624px;top:748px">Amber Kite Ductless Experts</h2>
  <p class="abs lorem about__text">Lorem ipsum dolor sit amet, consectetur adipiscing elit, sed do eiusmtempor incididunt ut labore et dolore magna aliqua. Ut enim ad minim veniam, quis nostrud exercitation ullamco laboris nisi ut aliquip ex ea commo consequat. Duis aute irure dolor in reprehenderit involuptate velit esse cillum dolore eu fugiat nulla pariatur. Excepteur sint occaecat cupidatat non proident, sunt in culpa qui officia deserunt mollit anim id est laborum.</p>
  <a class="btn" style="left:623px;top:1020px;width:155px;height:52px">Learn More</a>
</section>

<section class="cards">
  <article class="card" style="left:77px">
    <div class="card__img photo" role="img" aria-label="Technician checking an outdoor unit with a tablet"></div>
    <h3 class="card__title">Get Some Answers</h3>
    <a class="btn">Ductless FAQ</a>
  </article>
  <article class="card" style="left:433px">
    <div class="card__img photo" role="img" aria-label="Two workers in safety vests beside outdoor condenser units"></div>
    <h3 class="card__title">Our Financing Options</h3>
    <a class="btn">Financing</a>
  </article>
  <article class="card" style="left:790px">
    <div class="card__img photo" role="img" aria-label="Technician servicing a wall mounted mini split"></div>
    <h3 class="card__title">Stay Up To Date</h3>
    <a class="btn">Our Blog</a>
  </article>
</section>

<section class="services">
  <p class="eyebrow center" style="top:1592px">How We Can Help You?</p>
  <h2 class="heading center" style="top:1624px">We Provide Services</h2>

  <div class="service" style="left:77px">
    <div class="service__icon"><svg width="46" height="46" viewBox="0 0 46 46" fill="none" stroke="var(--yellow)" stroke-width="2"><circle cx="23" cy="20" r="7"/><path d="M4 34h10l8 4h16M4 12h10l8-4h16"/></svg></div>
    <h3 class="service__title">Ductless Installation</h3>
    <p class="service__text lorem">Lorem ipsum dolor sit amet, consectetur adipiscing elit, sed do labore et dolore magna aliqua.</p>
  </div>
  <div class="service" style="left:346px">
    <div class="service__icon is-active"><svg width="46" height="46" viewBox="0 0 46 46" fill="none" stroke="var(--ink)" stroke-width="2"><rect x="6" y="8" width="34" height="30" rx="3"/><path d="M6 16h34"/><circle cx="23" cy="27" r="6"/><path d="M23 19v2M23 33v2M15 27h2M29 27h2"/></svg></div>
    <h3 class="service__title">Ductless Maintenance</h3>
    <p class="service__text lorem">Lorem ipsum dolor sit amet, consectetur adipiscing elit, sed do labore et dolore magna aliqua.</p>
  </div>
  <div class="service" style="left:614px">
    <div class="service__icon"><svg width="46" height="46" viewBox="0 0 46 46" fill="none" stroke="var(--yellow)" stroke-width="2"><rect x="8" y="14" width="12" height="24" rx="2"/><path d="M14 8v6M28 8v30M34 8v30M26 20h10"/></svg></div>
    <h3 class="service__title">Ductless Repair</h3>
    <p class="service__text lorem">Lorem ipsum dolor sit amet, consectetur adipiscing elit, sed do labore et dolore magna aliqua.</p>
  </div>
  <div class="service" style="left:883px">
    <div class="service__icon"><svg width="46" height="46" viewBox="0 0 46 46" fill="none" stroke="var(--yellow)" stroke-width="2"><rect x="10" y="6" width="24" height="32" rx="2"/><path d="M15 14h14M15 20h14M15 26h9"/><circle cx="33" cy="33" r="5"/></svg></div>
    <h3 class="service__title">Ductless Warranty</h3>
    <p class="service__text lorem">Lorem ipsum dolor sit amet, consectetur adipiscing elit, sed do labore et dolore magna aliqua.</p>
  </div>

  <a class="btn" style="left:496px;top:2021px;width:207px;height:50px">View All Services</a>
</section>

<section class="why">
  <p class="eyebrow" style="left:80px;top:2133px">Why Choose Us?</p>
  <h2 class="heading" style="left:80px;top:2165px">We Provide Best Quality</h2>

  <div class="feature" style="top:2269px">
    <div class="feature__icon is-yellow"><svg width="44" height="44" viewBox="0 0 44 44" fill="none" stroke="var(--ink)" stroke-width="2"><path d="M6 20 22 7l16 13M10 18v18h24V18"/><text x="22" y="32" text-anchor="middle" font-family="Poppins" font-size="12" fill="var(--ink)" stroke="none">$</text></svg></div>
    <h3 class="feature__title">0% Financing for 60 months</h3>
    <p class="feature__text lorem">Lorem ipsum dolor sit amet, consectetur adipiscing elit, eiusmod tempor dolore magna aliqua.</p>
  </div>
  <div class="feature" style="top:2394px">
    <div class="feature__icon"><svg width="44" height="44" viewBox="0 0 44 44" fill="none" stroke="var(--white)" stroke-width="2"><rect x="6" y="10" width="26" height="10" rx="2"/><rect x="12" y="24" width="26" height="10" rx="2"/><circle cx="19" cy="15" r="2"/><circle cx="25" cy="29" r="2"/></svg></div>
    <h3 class="feature__title">365 Day, Money Back Guarantee</h3>
    <p class="feature__text lorem">Lorem ipsum dolor sit amet, consectetur adipiscing elit, eiusmod tempor dolore magna aliqua.</p>
  </div>
  <div class="feature" style="top:2519px">
    <div class="feature__icon"><svg width="44" height="44" viewBox="0 0 44 44" fill="none" stroke="var(--white)" stroke-width="2"><rect x="5" y="12" width="22" height="16" rx="2"/><path d="M27 17h7l5 6v5H27z"/><circle cx="13" cy="31" r="3"/><circle cx="33" cy="31" r="3"/></svg></div>
    <h3 class="feature__title">Experts in Ductless Services</h3>
    <p class="feature__text lorem">Lorem ipsum dolor sit amet, consectetur adipiscing elit, eiusmod tempor dolore magna aliqua.</p>
  </div>

  <div class="abs" style="left:662px;top:2132px;width:462px;height:470px;border-radius:50%;background:var(--yellow)"></div>
  <div class="abs photo" role="img" aria-label="Technician in a green cap opening the panel of an indoor air unit" style="left:652px;top:2132px;width:452px;height:452px;border-radius:50%"></div>
</section>

<section class="testimonial">
  <p class="eyebrow center" style="top:2663px">Client's Feedback</p>
  <h2 class="heading center" style="top:2695px">Customer Say About Us</h2>
  <div class="abs quote">
    <p class="quote__text">Lorem ipsum dolor sit amet, consectetur adipiscing elit, sed do eiusmod tempor incididunt ut labore et dolore magna aliqua. Ut enim ad minim veniam, quis nostrud Excepteur sint occaecat cupidatat non proident, sunt in culpa qui officia deserunt mollit anim id est laborum.</p>
    <p class="quote__name">-&nbsp; Client's Name</p>
    <svg class="abs" style="left:246px;top:283px" width="40" height="16" viewBox="0 0 40 16" fill="none" stroke="var(--ink)" stroke-width="1.6"><path d="M39 8H2M9 1 2 8l7 7"/></svg>
    <svg class="abs" style="left:486px;top:283px" width="40" height="16" viewBox="0 0 40 16" fill="none" stroke="var(--yellow)" stroke-width="1.6"><path d="M1 8h37M31 1l7 7-7 7"/></svg>
  </div>
  <div class="abs photo" role="img" aria-label="Portrait of a client" style="left:546px;top:3070px;width:106px;height:106px;border-radius:50%;border:4px solid var(--white);box-shadow:0 2px 8px rgba(0,0,0,.2)"></div>
</section>

<section class="newsletter">
  <div class="abs news">
    <h2 class="news__title">Subcribe Newsletter</h2>
    <p class="news__text">Lorem ipsum dolor sit amet, consectetur adipiscing elit, sed do eiusmod tempor incididunt ut labore et dolore magna aliqua.</p>
    <div class="news__field">
      <svg width="20" height="14" viewBox="0 0 20 14" fill="none" stroke="var(--yellow)" stroke-width="1.6"><rect x="1" y="1" width="18" height="12"/><path d="m1 1 9 7 9-7"/></svg>
      Enter Email here....
    </div>
    <a class="btn">Subscribe</a>
  </div>
  <div class="abs" style="left:78px;top:3238px;width:395px;height:395px;border-radius:50%;background:var(--yellow)"></div>
  <div class="abs photo" role="img" aria-label="Smiling technician writing on a clipboard beside a wall unit" style="left:84px;top:3240px;width:370px;height:370px;border-radius:50%"></div>
</section>

<footer>
  <div class="abs footer-brand"><span class="brand__dot"></span>Amber Kite Services</div>
  <p class="abs center footer-links">Home &nbsp;| &nbsp;About Us &nbsp;| &nbsp;Services &nbsp;| &nbsp;Why Choose Us? &nbsp;| &nbsp;Blog &nbsp;| &nbsp;Contact</p>
  <span class="social" style="left:526px;background:#3b5a9a" aria-label="Social link"></span>
  <span class="social" style="left:578px;background:#1a7bb9" aria-label="Social link"></span>
  <span class="social" style="left:630px;background:#3cb3e6" aria-label="Social link"></span>
  <div class="abs copyright"><span><b>© AMBER KITE DUCTLESS EXPERTS SERVICES</b> - 2019. All Rights Reserved.</span></div>
</footer>

</body>
</html>
```